Clinical Layout Builders - Stationery
Biz Cards + Stationary
Clinical Layout Builders - Stationery - Information Technology
Creative Brief
Professional
Dr. Elena M. Castillo
Director of Content Development
Ceiba Business Plaza #3, Suite 118 San Juan, PR 00941
(787) PENDING
elena.castillo@hnvwqbt.com
www.hnvwqbt.com
Need a second set of cards for: Dr. Luis F. Beltran Business Development Director Same info- address, fax and phone (Pending) Cell: (787) 555-0192 Email: luis.beltran@hnvwqbt.com
Either the logo, the website or something else. Feel free to be creative!

```html
<!DOCTYPE html>
<html lang="en">
<head>
<meta charset="utf-8">
<title>Clinical Layout Builders – Stationery</title>
<link rel="stylesheet" href="https://fonts.googleapis.com/css2?family=Roboto:wght@400;700&display=swap">
<style>
  :root{
    --bg:#4a3426;
    --paper:#ffffff;
    --magenta:#a8246f;
    --magenta-dark:#6e1048;
    --magenta-light:#d77fb0;
    --ink:#333333;
    --muted:#777777;
    --grey-flap:#8c8c8c;
    --black:#111111;
  }
  *{box-sizing:border-box;margin:0;padding:0}
  html,body{width:1200px;height:506px;overflow:hidden}
  body{background:var(--bg);font-family:"Roboto",Arial,sans-serif;color:var(--ink);position:relative}
  .piece{position:absolute;background:var(--paper);overflow:hidden;box-shadow:0 3px 8px rgba(0,0,0,.45)}
  .piece svg.shape{position:absolute;inset:0;width:100%;height:100%}
  .brand{position:absolute;font-weight:700;color:var(--magenta);white-space:nowrap;display:flex;align-items:center;gap:3px}
  .brand .mark{display:inline-block;background:var(--magenta);flex:none}
  .brand.on-dark{color:var(--paper)}
  .brand.on-dark .mark{background:var(--paper)}
  .brand.faint{color:var(--magenta-light);opacity:.35}
  .brand.faint .mark{background:var(--magenta-light)}

  /* business cards */
  .card{width:137px;height:82px}
  .card .name{position:absolute;top:7px;right:6px;font-size:5px;font-weight:700;color:var(--paper);text-align:right;white-space:nowrap}
  .card .role{display:block;font-size:3.6px;font-weight:400;margin-top:1px}
  .card .details{position:absolute;right:6px;top:38px;font-size:3.5px;line-height:1.45;text-align:right;color:var(--paper);white-space:nowrap}
  .card .web{position:absolute;left:0;right:0;bottom:7px;text-align:center;font-size:4.5px}
  .card-front-a{left:12px;top:108px}
  .card-front-b{left:156px;top:108px;background:var(--black)}
  .card-back-a{left:12px;top:212px}
  .card-back-b{left:156px;top:212px;background:var(--magenta)}

  /* letterhead */
  .letterhead{left:456px;top:29px;width:232px;height:300px}
  .letterhead .sender{position:absolute;top:14px;right:12px;font-size:4.5px;line-height:1.45;color:var(--muted);white-space:nowrap}

  /* envelopes */
  .envelope-front{left:612px;top:228px;width:282px;height:212px}
  .envelope-front .return{position:absolute;left:28px;top:152px;font-size:4.5px;line-height:1.45;color:var(--muted)}
  .envelope-back{left:912px;top:29px;width:281px;height:127px}
  .envelope-plain{left:912px;top:168px;width:281px;height:116px}
</style>
</head>
<body>

  <!-- business card: Elena, front -->
  <div class="piece card card-front-a">
    <svg class="shape" viewBox="0 0 137 82" preserveAspectRatio="none" aria-hidden="true">
      <path d="M66 0 H137 V82 H82 C102 55 52 30 66 0 Z" fill="var(--magenta)"/>
      <path d="M62 0 C48 30 98 55 78 82" fill="none" stroke="var(--magenta-dark)" stroke-width="0.8"/>
    </svg>
    <div class="brand" style="left:6px;top:30px;font-size:4.6px"><span class="mark" style="width:4px;height:4px"></span>Clinical Layout Builders</div>
    <div class="name">Dr. Elena M. Castillo<span class="role">Director of Content Development</span></div>
    <div class="details">Ceiba Business Plaza #3, Suite 118<br>San Juan, PR 00941<br>(787) PENDING<br>elena.castillo@hnvwqbt.com</div>
  </div>

  <!-- business card: Luis, front -->
  <div class="piece card card-front-b">
    <svg class="shape" viewBox="0 0 137 82" preserveAspectRatio="none" aria-hidden="true">
      <path d="M66 0 H137 V82 H82 C102 55 52 30 66 0 Z" fill="var(--magenta)"/>
    </svg>
    <div class="brand on-dark" style="left:6px;top:30px;font-size:4.6px"><span class="mark" style="width:4px;height:4px"></span>Clinical Layout Builders</div>
    <div class="name">Dr. Luis F. Beltran<span class="role">Business Development Director</span></div>
    <div class="details">Ceiba Business Plaza #3, Suite 118<br>San Juan, PR 00941<br>Cell: (787) 555-0192<br>luis.beltran@hnvwqbt.com</div>
  </div>

  <!-- business card backs -->
  <div class="piece card card-back-a">
    <div class="brand" style="left:14px;top:26px;font-size:9px"><span class="mark" style="width:7px;height:7px"></span>Clinical Layout Builders</div>
    <div class="web" style="color:var(--muted)">www.hnvwqbt.com</div>
  </div>
  <div class="piece card card-back-b">
    <div class="brand on-dark" style="left:14px;top:26px;font-size:9px"><span class="mark" style="width:7px;height:7px"></span>Clinical Layout Builders</div>
    <div class="web" style="color:var(--paper)">www.hnvwqbt.com</div>
  </div>

  <!-- letterhead -->
  <div class="piece letterhead">
    <svg class="shape" viewBox="0 0 232 300" preserveAspectRatio="none" aria-hidden="true">
      <path d="M0 150 C20 190 26 250 10 300 H0 Z" fill="var(--magenta)"/>
      <path d="M6 140 C30 190 32 250 16 300" fill="none" stroke="var(--black)" stroke-width="1.5"/>
    </svg>
    <div class="brand" style="left:14px;top:20px;font-size:9px"><span class="mark" style="width:7px;height:7px"></span>Clinical Layout Builders</div>
    <div class="sender">Ceiba Business Plaza #3, Suite 118<br>San Juan, PR 00941<br>(787) PENDING<br>www.hnvwqbt.com</div>
    <div class="brand faint" style="left:18px;top:120px;font-size:14px"><span class="mark" style="width:11px;height:11px"></span>Clinical Layout Builders</div>
  </div>

  <!-- envelope, front with flap -->
  <div class="piece envelope-front">
    <svg class="shape" viewBox="0 0 282 212" preserveAspectRatio="none" aria-hidden="true">
      <path d="M0 0 H282 V60 L170 112 C150 120 132 120 112 112 L0 60 Z" fill="var(--magenta)"/>
      <path d="M0 62 L112 114 C132 122 150 122 170 114 L282 62" fill="none" stroke="var(--magenta-dark)" stroke-width="1.5"/>
    </svg>
    <div class="brand on-dark" style="left:88px;top:58px;font-size:10px"><span class="mark" style="width:8px;height:8px"></span>Clinical Layout Builders</div>
    <div class="return">Ceiba Business Plaza #3, Suite 118<br>San Juan, PR 00941<br>(787) PENDING<br>www.hnvwqbt.com</div>
  </div>

  <!-- envelope, back with grey flap -->
  <div class="piece envelope-back">
    <svg class="shape" viewBox="0 0 281 127" preserveAspectRatio="none" aria-hidden="true">
      <path d="M0 0 H281 L150 60 C144 63 137 63 131 60 Z" fill="var(--grey-flap)"/>
    </svg>
    <div class="brand" style="left:84px;top:88px;font-size:10px"><span class="mark" style="width:8px;height:8px"></span>Clinical Layout Builders</div>
  </div>

  <!-- envelope, plain with flap outline -->
  <div class="piece envelope-plain">
    <svg class="shape" viewBox="0 0 281 116" preserveAspectRatio="none" aria-hidden="true">
      <path d="M0 0 L131 58 C137 61 144 61 150 58 L281 0" fill="none" stroke="#dddddd" stroke-width="1.5"/>
    </svg>
    <div class="brand" style="left:84px;top:14px;font-size:10px"><span class="mark" style="width:8px;height:8px"></span>Clinical Layout Builders</div>
  </div>

</body>
</html>
```